TrivoSuite – Veloura Flyer for Plexora (Harwick Travel Corporation)

Overview
Harwick Travel Corporation is launching a series of branded flyers to highlight the features and benefits of our TrivoSuite platform — our all-in-one corporate travel technology suite.
This first flyer will spotlight Veloura, our risk management and traveller safety solution, and will be published on Plexora as part of a digital awareness campaign.
⸻
Objective
Create a striking, professional, and modern flyer that communicates how Veloura enhances the TrivoSuite platform by ensuring traveller safety, communication, and real-time updates.
The design should feel premium, contemporary, and aligned with Harwick Travel’s luxury corporate identity.
⸻
Target Audience
• Corporate clients and travel decision-makers
• Travel managers, procurement teams, and executive assistants
• Existing Harwick Travel corporate partners on Plexora
⸻
Key Message
Veloura – Your travellers’ safety, visibility, and communication, all in one place.
Part of TrivoSuite, Harwick Travel’s integrated corporate travel platform.
⸻
Core Features to Highlight
• 24/7 real-time risk alerts
• Instant traveller identification and tracking by location or timeframe
• Two-way communication between traveller and company
• Integrated with travel itineraries for seamless care
• Supports duty-of-care compliance for corporate travel policies
⸻
Tone & Style
• Sophisticated, trusted, and innovative
• Clean lines, premium feel, and minimal clutter
• Should feel like a Harwick Travel-branded asset — not overly “techy”
• Imagery: travel safety, global maps, communication lines, or business travellers in motion
⸻
Design Direction
• Brand: Use Harwick Travel brand colours (gold, charcoal, white, navy)
• Typography: Professional, modern sans-serif fonts
• Logo: Include Harwick Travel and TrivoSuite logos (can supply if needed)
• CTA: “Discover Veloura on TrivoSuite” or “Set the Gold Standard of Corporate Travel”
• Layout: Ideal for Plexora post format (square or 4:5 vertical)
⸻
Deliverables
• Editable design file (AI / PSD / InDesign)
• Final exports for social media:
• 1080x1080 px (Plexora square)
• 1080x1350 px (Plexora portrait)
• Include space for light text overlay (for post captioning later)
⸻
Inspiration
• Style similar to luxury tech or premium corporate innovation brands
• Feel: clean, high-contrast, aspirational, minimal

```html
<!DOCTYPE html>
<html lang="en">
<head>
<meta charset="utf-8">
<title>TrivoSuite – Veloura Flyers</title>
<link rel="stylesheet" href="https://fonts.googleapis.com/css2?family=Outfit:wght@300;400;800&display=swap">
<style>
  :root {
    --navy: #0f2342;
    --gold: #dca163;
    --gold-deep: #b98147;
    --white: #ffffff;
    --photo-light: #9a9da0;
    --photo-dark: #3d434b;
    --page: #ffffff;
  }
  * { margin: 0; padding: 0; box-sizing: border-box; }
  html, body { width: 1200px; height: 757px; overflow: hidden; background: var(--page); }
  body { position: relative; font-family: "Outfit", sans-serif; color: var(--white); }

  .flyer { position: absolute; overflow: hidden; }
  .flyer--square { left: 46px; top: 48px; width: 525px; height: 525px; }
  .flyer--portrait { left: 629px; top: 48px; width: 525px; height: 656px; }

  .flyer__photo {
    position: absolute; inset: 0;
    background: linear-gradient(160deg, var(--photo-light) 0%, #6f747a 45%, var(--photo-dark) 100%);
  }
  .flyer__shapes { position: absolute; inset: 0; width: 100%; height: 100%; }

  .headline {
    position: absolute; text-align: center; display: flex; flex-direction: column; align-items: center;
    letter-spacing: -0.02em;
  }
  .headline__bold { font-weight: 800; }
  .headline__gold { color: var(--gold); }
  .headline__light { font-weight: 300; }
  .headline__of { display: flex; align-items: center; gap: 14px; font-weight: 300; }
  .headline__rule { display: block; height: 1px; background: rgba(255,255,255,0.55); }

  .flyer--square .headline { left: 262px; width: 256px; top: 60px; font-size: 47px; line-height: 49px; }
  .flyer--square .headline__rule { width: 68px; }
  .flyer--portrait .headline { left: 255px; width: 264px; top: 36px; font-size: 44px; line-height: 45px; }
  .flyer--portrait .headline__rule { width: 62px; }

  .features {
    position: absolute; left: 270px; width: 222px; top: 331px;
    list-style: none; text-align: center; font-size: 11.5px; line-height: 15px; font-weight: 300;
  }
  .features__item + .features__item::before {
    content: ""; display: block; width: 3px; height: 3px; border-radius: 50%;
    background: var(--gold); margin: 6px auto 6px;
  }

  .brand { position: absolute; text-align: center; }
  .brand__name { display: block; font-weight: 800; font-size: 35px; line-height: 34px; letter-spacing: -0.02em; }
  .brand__company { display: block; font-weight: 400; font-size: 12px; line-height: 14px; letter-spacing: 0.01em; text-transform: uppercase; }
  .flyer--square .brand { left: 232px; width: 200px; top: 449px; }
  .flyer--portrait .brand { left: 232px; width: 205px; top: 589px; }
</style>
</head>
<body>

<section class="flyer flyer--square">
  <div class="flyer__photo" role="img" aria-label="Businesswoman in a navy suit walking through an airport terminal with a suitcase and a leather bag"></div>
  <svg class="flyer__shapes" viewBox="0 0 875 875" preserveAspectRatio="none" aria-hidden="true">
    <defs>
      <linearGradient id="goldBandSq" x1="0" y1="0" x2="0" y2="1">
        <stop offset="0" stop-color="#e2a965"/>
        <stop offset="1" stop-color="#b98147"/>
      </linearGradient>
    </defs>
    <polygon points="440,0 875,0 875,710 378,710" fill="#0f2342"/>
    <polygon points="263,710 875,710 875,875 233,875" fill="url(#goldBandSq)"/>
  </svg>
  <h1 class="headline">
    <span class="headline__bold">Set the</span>
    <span class="headline__bold headline__gold">Gold</span>
    <span class="headline__bold headline__gold">Standard</span>
    <span class="headline__of"><span class="headline__rule"></span>of<span class="headline__rule"></span></span>
    <span class="headline__light">Corporate</span>
    <span class="headline__light">Travel</span>
  </h1>
  <div class="brand">
    <span class="brand__name">TrivoSuite</span>
    <span class="brand__company">Harwick Travel Corporation</span>
  </div>
</section>

<section class="flyer flyer--portrait">
  <div class="flyer__photo" role="img" aria-label="Businesswoman in a navy suit walking through an airport terminal with a suitcase and a leather bag"></div>
  <svg class="flyer__shapes" viewBox="0 0 875 1093" preserveAspectRatio="none" aria-hidden="true">
    <defs>
      <linearGradient id="goldBandPt" x1="0" y1="0" x2="0" y2="1">
        <stop offset="0" stop-color="#e2a965"/>
        <stop offset="1" stop-color="#b98147"/>
      </linearGradient>
    </defs>
    <polygon points="425,0 875,0 875,940 347,940" fill="#0f2342"/>
    <polygon points="274,940 875,940 875,1093 252,1093" fill="url(#goldBandPt)"/>
  </svg>
  <h2 class="headline">
    <span class="headline__bold">Set the</span>
    <span class="headline__bold headline__gold">Gold</span>
    <span class="headline__bold headline__gold">Standard</span>
    <span class="headline__of"><span class="headline__rule"></span>of<span class="headline__rule"></span></span>
    <span class="headline__light">Corporate</span>
    <span class="headline__light">Travel</span>
  </h2>
  <ul class="features">
    <li class="features__item">24/7 real-time risk alerts</li>
    <li class="features__item">Instant traveller identification and tracking by location or timeframe</li>
    <li class="features__item">Two-way communication between traveller and company</li>
    <li class="features__item">Integrated with travel itineraries for seamless care</li>
    <li class="features__item">Supports duty-of-care compliance for corporate travel policies</li>
  </ul>
  <div class="brand">
    <span class="brand__name">TrivoSuite</span>
    <span class="brand__company">Harwick Travel Corporation</span>
  </div>
</section>

</body>
</html>
```